Business Card Design - Photographer

I am a landscape photographer and I require a business card design. 

I require two designs:
1)  a double sided business card
 and
b)  a single sided business card 

The single sided design can either be the same as the double sided (with just one side having all the information)....or it can be an entire new design. Its up to you.

My corporate colours are (CMYK):

Blue   69, 32, 0, 0
Grey  72,  64,  47,  31
Green  32,  2,  91,  0
Yellow   0, 19, 92, 0
Orange  0, 39, 75, 0

Colour space in final file should be in CMYK.

The details that need to be included on the card:

- Use the provided Logo
- Name: Wiktor Nowiradzki
- Email:   sales@framesbywiktor.com.au
- Website:    framesbywiktor.com.au
- Twitter:    chatterline.com/framesbywiktor
- Facebook:   friendwall.com/framesbywiktor
- Mobile  0419 356 782

Please use the attached template to design the logo to the specified size, including the marked bleed lines. I have also attached my logo in PNG (transparent background) and ai format for you to use.

The final file should be:
- Photoshop version with layers so I can edit the name/text etc. All non vector files should be high resolution at 1039 x 697 pixels at 300 dpi.

I also require a file as:
- Vector based PDF

Anyway questions please contact me.

Thank you

Industry/Entity Type

Landscape

Logo styles of interest
Pictorial/Combination Logo
Abstract Logo
Wordmark Logo
Lettermark Logo
Requirements
Must have
• The details that need to be included on the card:

- Use the provided Logo
- Name: Wiktor Nowiradzki
- Email: sales@framesbywiktor.com.au
- Website: framesbywiktor.com.au
- Twitter: chatterline.com/framesbywiktor
- Facebook: friendwall.com/framesbywiktor
- Mobile 0419 356 782

```html
<!DOCTYPE html>
<html lang="en">
<head>
<meta charset="utf-8">
<title>Frames by Wiktor – Business Card</title>
<link rel="stylesheet" href="https://fonts.googleapis.com/css2?family=Questrial&display=swap">
<style>
  :root {
    --backdrop: #8d8d8f;
    --card-paper: #ecebe9;
    --ink: #3f3d4a;
    --ink-soft: #5a5866;
    --rule: #7d7b86;
    --photo-sky: #d9d9d9;
    --photo-sea: #8e969a;
    --photo-rock: #1f1f21;
    --brand-light: #f2f2f2;
  }
  * { box-sizing: border-box; margin: 0; padding: 0; }
  html, body {
    width: 1200px; height: 900px; overflow: hidden;
    background: var(--backdrop);
    font-family: "Questrial", "Century Gothic", sans-serif;
    color: var(--ink);
  }
  .sheet {
    position: relative; width: 1200px; height: 900px;
    display: flex; justify-content: center; align-items: center; gap: 60px;
  }
  .card {
    position: relative; width: 360px; height: 537px;
    background: var(--card-paper);
    box-shadow: 0 10px 30px rgba(0,0,0,.25);
    overflow: hidden;
  }
  /* Front */
  .card-front__photo {
    position: absolute; inset: 0;
    background: linear-gradient(180deg,
      var(--photo-sky) 0%, #a9a9ab 38%,
      var(--photo-sea) 48%, #5e6468 62%,
      #3a3c3f 78%, var(--photo-rock) 100%);
  }
  .card-front__brand {
    position: absolute; left: 0; right: 0; top: 400px;
    display: flex; align-items: center; justify-content: center; gap: 12px;
    color: var(--brand-light);
  }
  .brand-dot {
    width: 26px; height: 26px; border-radius: 50%;
    background: currentColor; opacity: .85; flex: none;
  }
  .brand-name {
    font-size: 22px; letter-spacing: 2px; text-transform: uppercase;
    white-space: nowrap;
  }
  /* Back */
  .card-back__brand {
    display: flex; align-items: center; justify-content: center; gap: 12px;
    margin-top: 72px; color: var(--ink);
  }
  .card-back__name {
    margin: 58px 30px 0; padding-bottom: 16px;
    font-size: 27px; font-weight: 400; color: var(--ink-soft);
    border-bottom: 1px solid var(--rule);
  }
  .contact-list {
    list-style: none; margin: 26px 30px 0;
    font-size: 16px; color: var(--ink-soft);
  }
  .contact-list li {
    display: flex; align-items: center; gap: 12px; height: 28px;
    white-space: nowrap;
  }
  .contact-list svg { width: 15px; height: 15px; flex: none; }
  .contact-list .contact-web {
    margin-top: 6px; font-size: 18px; font-weight: 700; color: var(--ink);
  }
</style>
</head>
<body>
<main class="sheet">
  <section class="card card-front">
    <div class="card-front__photo" role="img" aria-label="Black and white long-exposure seascape with dark rocks under an overcast sky"></div>
    <div class="card-front__brand">
      <span class="brand-dot"></span>
      <span class="brand-name">Frames by Wiktor</span>
    </div>
  </section>

  <section class="card card-back">
    <div class="card-back__brand">
      <span class="brand-dot"></span>
      <span class="brand-name">Frames by Wiktor</span>
    </div>
    <h1 class="card-back__name">Wiktor Nowiradzki</h1>
    <ul class="contact-list">
      <li>
        <svg viewBox="0 0 16 16" aria-hidden="true"><rect x="4" y="1" width="8" height="14" rx="1.5" fill="var(--ink)"/><rect x="5.5" y="3" width="5" height="7" fill="var(--card-paper)"/></svg>
        0419 356 782
      </li>
      <li>
        <svg viewBox="0 0 16 16" aria-hidden="true"><rect x="1" y="3" width="14" height="10" fill="var(--ink)"/><path d="M1 3 L8 9 L15 3" fill="none" stroke="var(--card-paper)" stroke-width="1.3"/></svg>
        sales@framesbywiktor.com.au
      </li>
      <li>
        <svg viewBox="0 0 16 16" aria-hidden="true"><rect x="1" y="1" width="14" height="14" rx="2" fill="var(--ink)"/></svg>
        chatterline.com/framesbywiktor
      </li>
      <li>
        <svg viewBox="0 0 16 16" aria-hidden="true"><rect x="1" y="1" width="14" height="14" rx="2" fill="var(--ink)"/></svg>
        friendwall.com/framesbywiktor
      </li>
      <li class="contact-web">
        <svg viewBox="0 0 16 16" aria-hidden="true"><circle cx="8" cy="8" r="7" fill="var(--ink)"/></svg>
        framesbywiktor.com.au
      </li>
    </ul>
  </section>
</main>
</body>
</html>
```